The Rounded Court Performer Image Design

We are a basketball training company with in-person and online courses and camps for players from 4th grade through college, plus coaches of all levels. We are looking for a modern design of "The Rounded Court Performer" as the attached quick sketch shows. The seven "elements" of the complete player include: 1. Basketball IQ 2. Leadership 3. Mindset 4. Skills 5. Athleticism 6. Habits and 7. Communication
We will plan to use this design on our website, social media, emails, etc. Please see our website at trevanhoops.com to learn more about us and our current branding, fonts, and colors. We prefer to use the orange hex #f15d22 and blacks and dark gray. Though we have teal on our current website, we are moving away from that color so you can leave that off any designs. Thanks!
Target Market(s)
Basketball players and coaches, parents

```html
<!DOCTYPE html>
<html lang="en">
<head>
<meta charset="utf-8">
<title>The Rounded Court Performer</title>
<link href="https://fonts.googleapis.com/css2?family=Roboto+Condensed:wght@700&family=Oswald:wght@600&display=swap" rel="stylesheet">
<style>
  :root {
    --brand-orange: #f15d22;
    --marker-orange: #e4572a;
    --label-gray: #8c8c8c;
    --line-gray: #9a9a9a;
    --court-light: #f7f7f7;
    --court-mid: #ececec;
    --placeholder-warm: rgba(241, 93, 34, 0.28);
    --placeholder-dark: rgba(43, 43, 43, 0.22);
  }
  * { margin: 0; padding: 0; box-sizing: border-box; }
  html, body { width: 1200px; height: 879px; overflow: hidden; background: #ffffff; }
  .poster {
    position: relative;
    width: 1200px;
    height: 879px;
    overflow: hidden;
    font-family: "Roboto Condensed", "Arial Narrow", sans-serif;
  }
  .court-backdrop {
    position: absolute;
    inset: 0;
    background: radial-gradient(ellipse at 50% 45%, var(--court-light) 0%, var(--court-mid) 100%);
  }
  .title {
    position: absolute;
    top: 106px;
    left: 0;
    width: 100%;
    text-align: center;
    font-family: "Oswald", "Roboto Condensed", sans-serif;
    font-weight: 600;
    font-size: 56px;
    line-height: 1;
    letter-spacing: 0.5px;
    color: var(--brand-orange);
    text-transform: uppercase;
  }
  .player-illustration {
    position: absolute;
    left: 371px;
    top: 262px;
    width: 313px;
    height: 567px;
    border-radius: 12px;
    background: linear-gradient(160deg, var(--placeholder-warm) 0%, var(--placeholder-dark) 100%);
  }
  .callouts {
    position: absolute;
    inset: 0;
    width: 1200px;
    height: 879px;
  }
  .callout-line { stroke: var(--line-gray); stroke-width: 1; fill: none; }
  .callout-underline { stroke: var(--marker-orange); stroke-width: 1.2; }
  .target-ring { stroke: var(--marker-orange); stroke-width: 1; fill: none; }
  .target-dot { fill: var(--marker-orange); }
  .label {
    position: absolute;
    font-weight: 700;
    font-size: 32px;
    line-height: 32px;
    color: var(--label-gray);
    white-space: nowrap;
  }
  .label--left { left: 233px; }
  .label--right { right: 233px; text-align: right; }
</style>
</head>
<body>
  <main class="poster">
    <div class="court-backdrop" role="img" aria-label="Faint outdoor basketball court with hoop, backboard and chain-link fence"></div>

    <h1 class="title">The Rounded Court Performer</h1>

    <div class="player-illustration" role="img" aria-label="Illustration of a basketball player in an orange jersey and black shorts dribbling a ball"></div>

    <svg class="callouts" viewBox="0 0 825 604" aria-hidden="true">
      <line class="callout-underline" x1="160" y1="222" x2="250" y2="222"/>
      <line class="callout-line" x1="250" y1="222" x2="385" y2="203"/>
      <line class="callout-underline" x1="160" y1="318" x2="235" y2="318"/>
      <line class="callout-line" x1="235" y1="318" x2="380" y2="290"/>
      <line class="callout-underline" x1="160" y1="415" x2="220" y2="415"/>
      <line class="callout-line" x1="220" y1="415" x2="265" y2="378"/>

      <line class="callout-underline" x1="518" y1="222" x2="665" y2="222"/>
      <line class="callout-line" x1="395" y1="206" x2="518" y2="222"/>
      <line class="callout-underline" x1="490" y1="318" x2="665" y2="318"/>
      <line class="callout-line" x1="412" y1="236" x2="490" y2="318"/>
      <line class="callout-underline" x1="545" y1="415" x2="665" y2="415"/>
      <line class="callout-line" x1="445" y1="354" x2="545" y2="415"/>
      <line class="callout-underline" x1="540" y1="512" x2="665" y2="512"/>
      <line class="callout-line" x1="397" y1="490" x2="540" y2="512"/>

      <g>
        <circle class="target-ring" cx="390" cy="208" r="24"/>
        <circle class="target-ring" cx="390" cy="208" r="16"/>
        <circle class="target-dot" cx="390" cy="208" r="2"/>
      </g>
      <g>
        <circle class="target-ring" cx="380" cy="290" r="28"/>
        <circle class="target-ring" cx="380" cy="290" r="18"/>
        <circle class="target-dot" cx="380" cy="290" r="2"/>
      </g>
      <g>
        <circle class="target-ring" cx="266" cy="378" r="18"/>
        <circle class="target-ring" cx="266" cy="378" r="11"/>
        <circle class="target-dot" cx="266" cy="378" r="2"/>
      </g>
      <g>
        <circle class="target-ring" cx="446" cy="356" r="18"/>
        <circle class="target-ring" cx="446" cy="356" r="11"/>
        <circle class="target-dot" cx="446" cy="356" r="2"/>
      </g>
      <g>
        <circle class="target-ring" cx="395" cy="490" r="22"/>
        <circle class="target-ring" cx="395" cy="490" r="14"/>
        <circle class="target-dot" cx="395" cy="490" r="2"/>
      </g>
    </svg>

    <div class="label label--left" style="top:286px">Mindset</div>
    <div class="label label--left" style="top:425px">Habits</div>
    <div class="label label--left" style="top:566px">Skills</div>

    <div class="label label--right" style="top:286px">Basketball IQ</div>
    <div class="label label--right" style="top:425px">Communication</div>
    <div class="label label--right" style="top:566px">Leadership</div>
    <div class="label label--right" style="top:707px">Athleticism</div>
  </main>
</body>
</html>
```